Velkaros Pendants

Brightmoor Studio is a growing wedding ring wholesaler/manufacturer based in NYC. We have recently teamed up with a cross designer from Greece and added their line of cross pendants to our product line. We would like to introduce the product to our customers. We are looking for a clean looking postcard. Is it possible to remove the style number and weights from the bottom right corner of each image?
We will provide wording, etc. upon request.

Thanks.
Updates

We would like all or most images to be on the postcard, front and back is fine. Thanks!!

Industry/Entity Type

Wedding

```html
<!DOCTYPE html>
<html lang="en">
<head>
<meta charset="utf-8">
<title>Velkaros Pendants – Postcard</title>
<link href="https://fonts.googleapis.com/css2?family=Tinos:ital,wght@0,400;1,400&display=swap" rel="stylesheet">
<style>
  :root {
    --page-bg: #f4f2ef;
    --card-shadow: rgba(0,0,0,0.35);
    --silver-light: #f7f7f8;
    --silver-mid: #d9dadc;
    --silver-dark: #b9babd;
    --taupe: #85736b;
    --ink: #111111;
    --white: #ffffff;
    --tile-bg: #ffffff;
    --grid-gap: #e6e6e6;
    --gold: #d9b54a;
    --gold-light: #f1dc8e;
    --steel: #b8bcc2;
    --steel-light: #eceef1;
    --rule: #b5b6b8;
  }
  * { box-sizing: border-box; margin: 0; padding: 0; }
  html, body { width: 1200px; height: 919px; overflow: hidden; }
  body {
    position: relative;
    background: var(--page-bg);
    font-family: "Tinos", "Times New Roman", serif;
    color: var(--ink);
  }

  /* Front of card */
  .card-front {
    position: absolute;
    left: 254px; top: 299px;
    width: 357px; height: 461px;
    background: linear-gradient(100deg, var(--silver-light) 0%, var(--silver-mid) 60%, var(--silver-dark) 100%);
    box-shadow: 3px 4px 8px var(--card-shadow);
    overflow: hidden;
  }
  .hero-cross {
    position: absolute;
    left: 0; top: 0;
    width: 200px; height: 110px;
    background: radial-gradient(ellipse at 40% 40%, rgba(255,255,255,0.95), rgba(205,206,209,0.4) 70%, transparent);
  }
  .brand-name {
    position: absolute;
    font-family: "Tinos", "Times New Roman", serif;
    font-weight: 400;
    color: var(--ink);
    white-space: nowrap;
  }
  .card-front .brand-name { right: 22px; top: 34px; font-size: 24px; }
  .footer-band {
    position: absolute;
    left: 0; right: 0; top: 283px; bottom: 0;
    background: var(--taupe);
  }
  .product-grid {
    position: absolute;
    left: 14px; top: 101px;
    width: 329px; height: 304px;
    background: var(--grid-gap);
    padding: 3px;
    display: grid;
    grid-template-columns: repeat(4, 1fr);
    grid-template-rows: repeat(4, 1fr);
    gap: 5px;
    box-shadow: 0 1px 4px rgba(0,0,0,0.3);
  }
  .product-tile {
    background: var(--tile-bg);
    display: flex; align-items: center; justify-content: center;
  }
  .product-photo { width: 36px; height: 62px; border-radius: 3px; }
  .product-photo.gold { background: linear-gradient(90deg, var(--gold), var(--gold-light), var(--gold)); }
  .product-photo.silver { background: linear-gradient(90deg, var(--steel), var(--steel-light), var(--steel)); }
  .front-tagline {
    position: absolute;
    left: 0; right: 0; top: 413px;
    text-align: center;
    font-style: italic;
    font-size: 16px;
    color: var(--white);
  }

  /* Back of card */
  .card-back {
    position: absolute;
    left: 627px; top: 403px;
    width: 460px; height: 357px;
    background: linear-gradient(180deg, var(--white) 0%, var(--silver-mid) 70%, var(--silver-dark) 100%);
    box-shadow: 3px 4px 8px var(--card-shadow);
    overflow: hidden;
  }
  .back-cross {
    position: absolute;
    left: 0; top: 0;
    width: 270px; height: 330px;
    background: radial-gradient(ellipse at 45% 35%, rgba(255,255,255,0.85), rgba(215,216,219,0.35) 65%, transparent);
  }
  .card-back .brand-name { left: 22px; top: 104px; font-size: 26px; }
  .back-tagline {
    position: absolute; left: 22px; top: 145px;
    font-size: 16px;
  }
  .phone {
    position: absolute; left: 65px; top: 182px;
    font-size: 18px; font-style: italic; letter-spacing: 0.5px;
  }
  .stamp-box {
    position: absolute; left: 363px; top: 24px;
    width: 77px; height: 77px;
    border: 1px solid var(--rule);
  }
  .address-line {
    position: absolute; left: 265px;
    width: 175px; height: 1px;
    background: var(--rule);
  }
</style>
</head>
<body>
  <section class="card-front" aria-label="Postcard front">
    <div class="hero-cross" role="img" aria-label="Close-up photo of a diamond-set cross pendant"></div>
    <span class="brand-name">Velkaros Pendants</span>
    <div class="footer-band"></div>
    <div class="product-grid">
      <div class="product-tile"><div class="product-photo gold" role="img" aria-label="Gold cross pendant photo"></div></div>
      <div class="product-tile"><div class="product-photo silver" role="img" aria-label="White gold cross pendant photo"></div></div>
      <div class="product-tile"><div class="product-photo gold" role="img" aria-label="Gold cross pendant photo"></div></div>
      <div class="product-tile"><div class="product-photo silver" role="img" aria-label="White gold cross pendant photo"></div></div>
      <div class="product-tile"><div class="product-photo silver" role="img" aria-label="White gold cross pendant photo"></div></div>
      <div class="product-tile"><div class="product-photo gold" role="img" aria-label="Gold cross pendant photo"></div></div>
      <div class="product-tile"><div class="product-photo silver" role="img" aria-label="White gold cross pendant photo"></div></div>
      <div class="product-tile"><div class="product-photo gold" role="img" aria-label="Gold cross pendant photo"></div></div>
      <div class="product-tile"><div class="product-photo gold" role="img" aria-label="Gold cross pendant photo"></div></div>
      <div class="product-tile"><div class="product-photo silver" role="img" aria-label="White gold cross pendant photo"></div></div>
      <div class="product-tile"><div class="product-photo gold" role="img" aria-label="Gold cross pendant photo"></div></div>
      <div class="product-tile"><div class="product-photo silver" role="img" aria-label="White gold cross pendant photo"></div></div>
      <div class="product-tile"><div class="product-photo silver" role="img" aria-label="White gold cross pendant photo"></div></div>
      <div class="product-tile"><div class="product-photo gold" role="img" aria-label="Gold cross pendant photo"></div></div>
      <div class="product-tile"><div class="product-photo silver" role="img" aria-label="White gold cross pendant photo"></div></div>
      <div class="product-tile"><div class="product-photo gold" role="img" aria-label="Gold cross pendant photo"></div></div>
    </div>
    <p class="front-tagline">Handmade Designer Crosses</p>
  </section>

  <section class="card-back" aria-label="Postcard back">
    <div class="back-cross" role="img" aria-label="Faint photo of a diamond-set cross pendant"></div>
    <span class="brand-name">Velkaros Pendants</span>
    <p class="back-tagline">Handmade Designer Crosses</p>
    <p class="phone">800.555.0142</p>
    <div class="stamp-box"></div>
    <div class="address-line" style="top:175px"></div>
    <div class="address-line" style="top:207px"></div>
    <div class="address-line" style="top:239px"></div>
  </section>
</body>
</html>
```